Gift Card and Gift Card Holder Design

Hello I need a design for a gift card and the gift card holder. I am uploading two PDFs for examples of designs we used for other promotional flyers. I am also uploading some design templates - two gift card holder templates (each would require the same design) and one gift card template. Also attached are two images of another gift card design - simple front, back had areas for text. We will need these areas for text in the design. We will provide copy for those areas but we should be able to edit following the close of the design project with you.

Font styles to use
Sans Serif

Colors
ec1f27
0455a3

Requirements
Must have
• use this web site for color reference: https://brq7fitworks.com/
• use this website for design inspiration for custom gift card holders: https://plimvaleprints.com/customgiftcardholder.html
• option with $75 on front of card as value
• two more options without

```html
<!DOCTYPE html>
<html lang="en">
<head>
<meta charset="utf-8">
<title>Kestrel Window Blinds Gift Card</title>
<link rel="stylesheet" href="https://fonts.googleapis.com/css2?family=Anton&family=Archivo+Black&family=Nunito+Sans:wght@800;900&display=swap">
<style>
  :root {
    --brand-red: #a30000;
    --brand-red-deep: #6e0b12;
    --brand-blue: #0418cf;
    --brand-blue-deep: #0a2a7a;
    --white: #ffffff;
    --slot: #1b1c1c;
    --wood-light: #b8b3ab;
    --wood-mid: #8a847c;
    --wood-dark: #5f5853;
    --seam: #1f1d1c;
  }
  * { margin: 0; padding: 0; box-sizing: border-box; }
  html, body { width: 1200px; height: 754px; overflow: hidden; background: var(--white); }
  .card {
    position: relative;
    width: 1200px;
    height: 754px;
    overflow: hidden;
  }
  .backdrop {
    position: absolute;
    inset: 0;
    background:
      radial-gradient(ellipse at 55% 35%, rgba(220,222,215,0.55), rgba(220,222,215,0) 60%),
      linear-gradient(180deg, var(--wood-light) 0%, var(--wood-mid) 55%, var(--wood-dark) 100%);
  }
  .plank-seam {
    position: absolute;
    top: 0;
    width: 3px;
    height: 754px;
    background: var(--seam);
    opacity: 0.75;
  }
  .brand-mark {
    position: absolute;
    left: 44px;
    top: 140px;
    display: flex;
    align-items: center;
    gap: 12px;
  }
  .brand-mark__square {
    width: 46px;
    height: 46px;
    background: var(--brand-red);
  }
  .brand-mark__name {
    font-family: "Archivo Black", sans-serif;
    font-size: 50px;
    line-height: 1;
    color: var(--brand-blue);
  }
  .brand-tagline {
    position: absolute;
    left: 45px;
    top: 294px;
    font-family: "Nunito Sans", sans-serif;
    font-weight: 900;
    font-size: 33px;
    line-height: 1.1;
    letter-spacing: 0.5px;
    color: var(--white);
    text-shadow: 2px 2px 3px rgba(0,0,0,0.6);
    white-space: nowrap;
  }
  .slot {
    position: absolute;
    background: var(--slot);
  }
  .slot--top { left: 502px; top: 67px; width: 199px; height: 44px; border-radius: 22px; }
  .slot--side { left: 1090px; top: 278px; width: 43px; height: 198px; border-radius: 22px; }
  .slot--hole { left: 45px; top: 625px; width: 88px; height: 88px; border-radius: 50%; }
  .company-name {
    position: absolute;
    left: 387px;
    top: 138px;
    font-family: "Archivo Black", sans-serif;
    font-size: 58px;
    line-height: 1;
    color: var(--brand-blue);
    white-space: nowrap;
  }
  .company-line {
    position: absolute;
    left: 388px;
    top: 190px;
    font-family: "Nunito Sans", sans-serif;
    font-weight: 900;
    font-size: 16.6px;
    letter-spacing: 0.4px;
    color: var(--white);
    text-shadow: 1px 1px 2px rgba(0,0,0,0.7);
    white-space: nowrap;
  }
  .card-title {
    position: absolute;
    left: 298px;
    top: 458px;
    font-family: "Anton", sans-serif;
    font-size: 155px;
    line-height: 1;
    letter-spacing: 3px;
    white-space: nowrap;
    filter: drop-shadow(3px 3px 3px rgba(0,0,0,0.55));
  }
  .card-title__gift {
    background: linear-gradient(180deg, var(--brand-red) 0%, var(--brand-red-deep) 100%);
    -webkit-background-clip: text;
    background-clip: text;
    color: transparent;
  }
  .card-title__card {
    background: linear-gradient(180deg, var(--brand-blue) 0%, var(--brand-blue-deep) 100%);
    -webkit-background-clip: text;
    background-clip: text;
    color: transparent;
  }
</style>
</head>
<body>
  <main class="card">
    <div class="backdrop" role="img" aria-label="Faded photo of a bright living room with tall windows, a low table and chairs, overlaid on weathered wooden planks"></div>
    <div class="plank-seam" style="left:152px"></div>
    <div class="plank-seam" style="left:608px"></div>

    <div class="brand-mark">
      <span class="brand-mark__square"></span>
      <span class="brand-mark__name">Kestrel</span>
    </div>
    <p class="brand-tagline">Installed Solutions</p>

    <span class="slot slot--top"></span>
    <span class="slot slot--side"></span>
    <span class="slot slot--hole"></span>

    <h1 class="company-name">Kestrel Window Blinds</h1>
    <p class="company-line">The preferred installer of window treatments to the builder, homeowner, and remodelers.</p>

    <h2 class="card-title"><span class="card-title__gift">GIFT</span> <span class="card-title__card">CARD</span></h2>
  </main>
</body>
</html>
```